Breezeway Comfort business cards design

Need a business card design for a Heating and Air Conditioning business. I need these items included.
Business name: Breezeway Comfort
Owner: Marcus Tollefsen
License # 2874590
Phone number # 555-382-4071
Email: breezewaycomfortair@mailvista.example
Sales
Service
Installation
Maintenance

Heating and Air Conditioning

Requirements
Must have
• Company name , license number , phone number , email

```html
<!DOCTYPE html>
<html lang="en">
<head>
<meta charset="utf-8">
<title>Breezeway Comfort – Business Cards</title>
<link href="https://fonts.googleapis.com/css2?family=Barlow:wght@400;500;600;700&display=swap" rel="stylesheet">
<style>
  :root {
    --page-bg: #e9e7e4;
    --brand-blue: #2147a8;
    --brand-blue-light: #6482c4;
    --brand-orange: #f07a2c;
    --card-white: #f5f5f5;
    --ink: #1c1c1c;
    --white: #ffffff;
  }
  * { margin: 0; padding: 0; box-sizing: border-box; }
  html, body {
    width: 1200px; height: 900px; overflow: hidden;
    background: var(--page-bg);
    font-family: "Barlow", Arial, sans-serif;
  }
  .sheet {
    width: 1200px; height: 900px;
    display: flex; flex-direction: column;
    align-items: center; justify-content: center; gap: 48px;
  }
  .card {
    position: relative;
    width: 620px; height: 354px;
    border-radius: 18px;
    overflow: hidden;
    box-shadow: 0 6px 18px rgba(0,0,0,0.18);
  }

  /* Front */
  .card-front {
    background: linear-gradient(90deg, var(--brand-blue-light) 0%, var(--brand-blue) 62%, var(--brand-blue) 100%);
    color: var(--white);
  }
  .front-brand {
    position: absolute; left: 76px; top: 112px;
    display: flex; align-items: center; gap: 18px;
  }
  .brand-dot {
    width: 54px; height: 54px; border-radius: 50%;
    background: var(--brand-orange);
    flex: none;
  }
  .front-name {
    font-weight: 600; font-size: 40px; line-height: 1;
    letter-spacing: 2px; text-transform: uppercase;
    color: var(--white);
  }
  .front-tagline {
    position: absolute; left: 148px; top: 168px;
    font-weight: 500; font-size: 22px; letter-spacing: 8px;
    text-transform: uppercase;
  }
  .front-services {
    position: absolute; left: 76px; bottom: 38px;
    font-weight: 500; font-size: 18px; letter-spacing: 1px;
  }

  /* Back */
  .card-back { background: var(--card-white); color: var(--ink); }
  .back-brand {
    position: absolute; right: 36px; top: 40px;
    display: flex; align-items: center; gap: 12px;
  }
  .back-brand .brand-dot { width: 34px; height: 34px; }
  .back-name {
    font-weight: 600; font-size: 28px; letter-spacing: 1.5px;
    text-transform: uppercase; color: var(--brand-blue);
  }
  .contact {
    position: absolute; left: 56px; top: 176px;
  }
  .person-name {
    font-weight: 700; font-size: 28px; letter-spacing: 1px;
    color: var(--brand-blue); text-transform: uppercase; line-height: 1;
  }
  .person-role {
    display: inline-block; margin-top: 4px;
    font-size: 17px; padding-bottom: 3px;
    border-bottom: 2px solid var(--brand-orange);
  }
  .contact-list { list-style: none; margin-top: 14px; }
  .contact-list li {
    display: flex; align-items: center; gap: 10px;
    font-size: 18px; font-weight: 500; line-height: 1.55;
    letter-spacing: 0.5px;
  }
  .contact-list svg { width: 15px; height: 15px; fill: var(--ink); flex: none; }
  .license { margin-top: 10px; font-size: 18px; font-weight: 500; letter-spacing: 0.5px; }
</style>
</head>
<body>
<main class="sheet">
  <section class="card card-front" aria-label="Card front">
    <div class="front-brand">
      <span class="brand-dot"></span>
      <span class="front-name">Breezeway Comfort</span>
    </div>
    <p class="front-tagline">Heating &amp; Air</p>
    <p class="front-services">Sales | Service | Installation | Maintenance</p>
  </section>

  <section class="card card-back" aria-label="Card back">
    <div class="back-brand">
      <span class="brand-dot"></span>
      <span class="back-name">Breezeway Comfort</span>
    </div>
    <div class="contact">
      <h1 class="person-name">Marcus Tollefsen</h1>
      <span class="person-role">Owner</span>
      <ul class="contact-list">
        <li>
          <svg viewBox="0 0 24 24" aria-hidden="true"><path d="M6.6 10.8a15.1 15.1 0 0 0 6.6 6.6l2.2-2.2a1 1 0 0 1 1-.25 11.4 11.4 0 0 0 3.6.57 1 1 0 0 1 1 1V20a1 1 0 0 1-1 1A17 17 0 0 1 3 4a1 1 0 0 1 1-1h3.5a1 1 0 0 1 1 1c0 1.25.2 2.45.57 3.57a1 1 0 0 1-.25 1z"/></svg>
          555-382-4071
        </li>
        <li>
          <svg viewBox="0 0 24 24" aria-hidden="true"><path d="M2 5h20v14H2zm2 2v.5l8 5 8-5V7zm0 2.8V17h16V9.8l-8 5z"/></svg>
          breezewaycomfortair@mailvista.example
        </li>
      </ul>
      <p class="license">License # 2874590</p>
    </div>
  </section>
</main>
</body>
</html>
```